Financial Research Company Brand Ad

We need a poster design for "Varnholt Analytics" 254mm(h) x 190mm (w) Our research focuses on banks, bank credit, liquidity & corporate solvency. Our believes "Get the credit & liquidity trends right & the rest follows" Please see our website for more information. www.varnholt-analytics.example

Industry/Entity Type

Bank

```html
<!DOCTYPE html>
<html lang="en">
<head>
<meta charset="utf-8">
<title>Varnholt Analytics – Poster</title>
<link rel="stylesheet" href="https://fonts.googleapis.com/css2?family=Open+Sans:wght@700&family=Roboto+Condensed:wght@300;400;700&display=swap">
<style>
  :root {
    --space-top: #1d3a44;
    --space-mid: #16243a;
    --space-deep: #0a0f1c;
    --band-glass: rgba(235, 238, 242, 0.62);
    --band-edge: rgba(120, 125, 135, 0.75);
    --ink: #0b0b0b;
    --navy: #13237a;
    --navy-band: #0f2380;
    --address: #223c92;
    --paper: #ffffff;
    --paper-grey: #e6e7e8;
    --rule: #9a9a9a;
  }
  html, body {
    margin: 0;
    padding: 0;
    overflow: hidden;
    background: #ffffff;
  }
  .poster {
    position: relative;
    width: 898px;
    height: 1200px;
    overflow: hidden;
    background: var(--space-deep);
  }
  .space-backdrop {
    position: absolute;
    inset: 0;
    background: linear-gradient(180deg, var(--space-top) 0%, var(--space-mid) 45%, var(--space-deep) 100%);
  }
  .brand-band {
    position: absolute;
    left: 0;
    top: 238px;
    width: 898px;
    height: 160px;
    background: var(--band-glass);
    border-top: 12px solid var(--band-edge);
    border-bottom: 12px solid var(--band-edge);
    box-sizing: border-box;
  }
  .brand-disc {
    position: absolute;
    left: 110px;
    top: 218px;
    width: 192px;
    height: 192px;
    border-radius: 50%;
    background: rgba(240, 242, 245, 0.85);
  }
  .brand-name {
    position: absolute;
    left: 350px;
    top: 286px;
    margin: 0;
    font-family: "Open Sans", sans-serif;
    font-weight: 700;
    font-size: 56px;
    line-height: 1;
    color: var(--ink);
    letter-spacing: -0.5px;
    white-space: nowrap;
  }
  .focus-disc {
    position: absolute;
    left: -3px;
    top: 628px;
    width: 904px;
    height: 904px;
    border-radius: 50%;
    background: linear-gradient(180deg, var(--paper) 0%, var(--paper) 30%, var(--paper-grey) 60%);
  }
  .focus-list {
    position: absolute;
    left: 0;
    top: 730px;
    width: 898px;
    margin: 0;
    padding: 0;
    list-style: none;
  }
  .focus-rule {
    position: absolute;
    left: 50%;
    height: 4px;
    transform: translateX(-50%);
    border-radius: 50%;
    background: radial-gradient(ellipse at center, var(--rule), rgba(154,154,154,0) 70%);
  }
  .focus-item {
    position: absolute;
    left: 0;
    width: 898px;
    text-align: center;
    font-family: "Roboto Condensed", sans-serif;
    font-weight: 400;
    font-size: 27px;
    line-height: 1;
    color: var(--navy);
  }
  .web-band {
    position: absolute;
    left: 0;
    top: 1028px;
    width: 898px;
    height: 84px;
    background: var(--navy-band);
    display: flex;
    align-items: center;
    justify-content: center;
    font-family: "Roboto Condensed", sans-serif;
    font-weight: 700;
    font-size: 31px;
    color: #ffffff;
    letter-spacing: 0.2px;
  }
  .contact {
    position: absolute;
    left: 0;
    top: 1126px;
    width: 898px;
    text-align: center;
    font-family: "Roboto Condensed", sans-serif;
    font-weight: 300;
    font-size: 22px;
    line-height: 31px;
    font-style: normal;
    color: var(--address);
  }
  .contact p { margin: 0; }
  .contact .sep { margin: 0 14px; }
</style>
</head>
<body>
  <main class="poster">
    <div class="space-backdrop" role="img" aria-label="Starry deep-space nebula in teal and violet clouds"></div>

    <div class="brand-band"></div>
    <div class="brand-disc"></div>
    <h1 class="brand-name">Varnholt Analytics</h1>

    <div class="focus-disc"></div>
    <ul class="focus-list">
      <li class="focus-rule" style="top:4px;width:512px"></li>
      <li class="focus-item" style="top:32px">Banks</li>
      <li class="focus-rule" style="top:72px;width:640px"></li>
      <li class="focus-item" style="top:98px">Bank Credit</li>
      <li class="focus-rule" style="top:140px;width:690px"></li>
      <li class="focus-item" style="top:166px">Liquidity</li>
      <li class="focus-rule" style="top:208px;width:744px"></li>
      <li class="focus-item" style="top:232px">Corporate Solvency</li>
    </ul>

    <div class="web-band">www.varnholt-analytics.example</div>

    <address class="contact">
      <p>Marlowe House 512 47 Quayside Road. Central, Hong Kong</p>
      <p>Tel: +852 5550 0123<span class="sep">|</span>mara@varnholt-analytics.example</p>
    </address>
  </main>
</body>
</html>
```